Initial website for sport tech startup

We are currently in the R&D phases of our new product. It’s a headband to prevent concussion in the soccer market initially.

We have 2 products, one that’s basic aimed at the youth market and the other more technology driven that’s aimed at the academies and professional market.

Initially the product will launch in the UK

Target Market(s)

Youth soccer players and parents in UK, Soccer Clubs, Federations.

Industry/Entity Type

Sporting Good

Coding

Coded - Design and coding required

Number of Pages Required

5+ page

Requirements
Must have
• Professional style that can be adapted and changed over the coming months.
Nice to have
• Ecommerce ability in the future.

```html
<!DOCTYPE html>
<html lang="en">
<head>
<meta charset="utf-8">
<title>Helmora – Safety for the beautiful game</title>
<link href="https://fonts.googleapis.com/css2?family=IBM+Plex+Sans:wght@400;500;600;700&family=Rubik:wght@700&family=Nunito+Sans:wght@400;600&display=swap" rel="stylesheet">
<style>
:root{
  --blue:#1e8ad6;
  --blue-mid:#3399dd;
  --blue-light:#4aa5e0;
  --navy:#1d4f7c;
  --ink:#222;
  --text:#3a3a3a;
  --paper:#ffffff;
  --mist:#f3f0f0;
  --card-border:#e6e2e2;
}
*{box-sizing:border-box;margin:0;padding:0}
html,body{width:1200px;height:3813px;overflow:hidden;background:var(--paper)}
body{position:relative;font-family:"Nunito Sans",sans-serif;color:var(--text)}
.abs{position:absolute}
.heading{font-family:"IBM Plex Sans",sans-serif}

/* header */
.site-header{top:0;left:0;width:1200px;height:111px;background:var(--paper)}
.brand{left:132px;top:26px;font-family:"IBM Plex Sans",sans-serif;font-weight:600;font-size:54px;letter-spacing:3px;color:var(--navy);line-height:60px}
.contact-chip{top:28px;display:flex;gap:12px;align-items:center}
.chip-icon{width:27px;height:27px;border-radius:50%;background:var(--blue);display:flex;align-items:center;justify-content:center}
.chip-label{font-family:"IBM Plex Sans",sans-serif;font-size:10px;font-weight:500;color:var(--ink);line-height:12px}
.chip-value{font-family:"IBM Plex Sans",sans-serif;font-size:18px;color:var(--ink);line-height:22px}
.main-nav{top:74px;left:552px;display:flex;align-items:center;font-family:"IBM Plex Sans",sans-serif;font-size:13px;font-weight:500;color:var(--ink)}
.main-nav span{margin-right:32px}
.main-nav .current{background:var(--blue);color:#fff;padding:6px 8px;margin-right:24px}

/* hero */
.hero{top:111px;left:0;width:1200px;height:567px;background:radial-gradient(ellipse at 55% 35%,#7a6c5e 0%,#3c3a35 45%,#1e2420 100%)}
.hero-lower{position:absolute;left:0;bottom:0;width:100%;height:120px;background:linear-gradient(0deg,#7d1a1e 0%,rgba(90,30,30,0) 100%)}
.hero-panel{top:281px;left:873px;width:327px;height:240px;background:rgba(20,20,20,.78)}
.hero-title{position:absolute;left:28px;top:20px;font-family:"Rubik",sans-serif;font-weight:700;font-size:37px;line-height:38px;color:#fff;text-transform:uppercase}
.btn{display:inline-block;font-family:"IBM Plex Sans",sans-serif;font-weight:700;font-size:13px;letter-spacing:.3px;text-transform:uppercase}
.btn-solid{background:var(--blue);color:#fff}
.hero-panel .btn{position:absolute;left:30px;top:187px;width:111px;height:37px;line-height:37px;text-align:center}
.dots{top:635px;left:557px;display:flex;gap:12px;align-items:center}
.dots i{width:7px;height:7px;border-radius:50%;background:#fff}
.dots i.on{width:12px;height:12px;border:2px solid #fff;background:var(--blue)}

/* mission */
.mission{top:678px;left:0;width:1200px;height:456px;background:var(--blue)}
.mission-photo{position:absolute;left:0;top:0;width:600px;height:456px;background:linear-gradient(90deg,#0c2a4a 0%,#15508a 55%,var(--blue) 100%)}
.tag{position:absolute;font-family:"IBM Plex Sans",sans-serif;font-weight:700;text-transform:uppercase;border:2px solid}
.tag-light{color:#fff;border-color:#fff;font-size:15px;padding:3px 8px;letter-spacing:.4px}
.mission .tag{left:620px;top:49px}
.mission h2{position:absolute;left:620px;top:100px;font-family:"IBM Plex Sans",sans-serif;font-weight:700;font-size:25px;line-height:29px;color:#fff;text-transform:uppercase;width:440px}
.rule{position:absolute;left:620px;top:169px;width:44px;height:3px;background:#fff}
.mission p{position:absolute;left:620px;top:202px;width:440px;font-size:14px;line-height:19.2px;color:#fff}
.btn-white{background:#fff;color:var(--blue)}
.mission .btn{position:absolute;left:622px;top:370px;width:99px;height:35px;line-height:35px;text-align:center}

/* product */
.product{top:1134px;left:0;width:1200px;height:519px}
.tag-blue{color:var(--blue);border-color:var(--blue);font-size:22px;padding:2px 6px;letter-spacing:.3px}
.product .tag{left:132px;top:49px}
.product h3{position:absolute;left:132px;top:110px;width:390px;font-family:"IBM Plex Sans",sans-serif;font-weight:500;font-size:24px;line-height:28.5px;color:var(--ink)}
.product p{position:absolute;left:132px;top:254px;width:430px;font-size:14px;line-height:19.2px;color:var(--text)}
.product .btn{position:absolute;left:135px;top:433px;width:111px;height:36px;line-height:36px;text-align:center}
.product-art{position:absolute;left:620px;top:124px;width:462px;height:274px;border-radius:40px 60px 90px 120px;background:linear-gradient(135deg,#4b4f57 0%,#2f3238 100%)}

/* benefit band */
.benefits{top:1653px;left:0;width:1200px;height:147px;display:flex}
.benefit{height:147px;display:flex;align-items:center;justify-content:center;gap:20px;color:#fff;font-family:"IBM Plex Sans",sans-serif;font-weight:600;font-size:15px;line-height:19.5px}
.benefit:nth-child(1){width:400px;background:var(--blue)}
.benefit:nth-child(2){width:405px;background:var(--blue-mid)}
.benefit:nth-child(3){width:395px;background:var(--blue-light)}

/* features */
.features{top:1800px;left:0;width:1200px;height:635px;background:var(--mist)}
.section-tag{left:50%;transform:translateX(-50%)}
.features .tag{top:53px}
.feature-grid{position:absolute;left:104px;top:146px;display:grid;grid-template-columns:repeat(5,191px);grid-template-rows:233px 184px;column-gap:14px;row-gap:14px}
.feature{background:#fff;box-shadow:0 1px 3px rgba(0,0,0,.08);text-align:center;padding:26px 24px 0;font-size:12.3px;line-height:16px;color:var(--ink)}
.feature svg{display:block;margin:0 auto 22px}

/* team */
.team{top:2435px;left:0;width:1200px;height:654px}
.team .tag{top:63px}
.member{position:absolute;top:208px;width:295px;height:358px;border:2px solid #555;text-align:center}
.portrait{position:absolute;left:50%;top:-56px;transform:translateX(-50%);width:163px;height:163px;border-radius:50%}
.member h4{position:absolute;top:136px;width:100%;font-family:"IBM Plex Sans",sans-serif;font-weight:700;font-size:16px;color:var(--ink);text-transform:uppercase;letter-spacing:.3px}
.member .role{position:absolute;top:160px;width:100%;font-size:12px;color:var(--ink)}
.member p{position:absolute;top:190px;left:40px;right:40px;font-size:12px;line-height:16px;color:var(--ink)}
.member .btn{position:absolute;left:50%;bottom:-10px;transform:translateX(-50%);font-size:12px;padding:2px 12px}

/* distribution */
.distribution{top:3089px;left:0;width:1200px;height:323px}
.distribution .tag{top:56px}
.distribution p{position:absolute;top:123px;left:200px;width:800px;text-align:center;font-size:14.3px;line-height:19px;color:var(--ink)}
.partner{position:absolute;top:201px;height:60px}

/* footer */
.site-footer{top:3412px;left:0;width:1200px;height:401px;background:var(--blue);color:#fff}
.site-footer .brand{position:absolute;left:132px;top:72px;color:#fff}
.col-title{position:absolute;top:52px;font-family:"IBM Plex Sans",sans-serif;font-weight:700;font-size:15px;letter-spacing:.5px}
.menu-list{position:absolute;left:488px;top:98px;font-family:"IBM Plex Sans",sans-serif;font-size:14px;line-height:24px}
.foot-item{position:absolute;display:flex;align-items:center;gap:14px;font-family:"IBM Plex Sans",sans-serif;font-size:14px;line-height:18px}
.foot-icon{width:27px;height:27px;border-radius:50%;background:#fff;display:flex;align-items:center;justify-content:center;flex:none}
.copyright{position:absolute;top:351px;width:1200px;left:-198px;text-align:center;font-size:11px}
</style>
</head>
<body>

<header class="site-header abs">
  <div class="brand abs">HELMORA</div>
  <div class="contact-chip abs" style="left:695px">
    <div class="chip-icon"><svg width="13" height="10" viewBox="0 0 13 10"><rect x=".5" y=".5" width="12" height="9" fill="#fff"/><path d="M.5 .5l6 5 6-5" stroke="#1e8ad6" fill="none"/></svg></div>
    <div><div class="chip-label">E MAIL US</div><div class="chip-value">info@helmora.com</div></div>
  </div>
  <div class="contact-chip abs" style="left:913px">
    <div class="chip-icon"><svg width="12" height="12" viewBox="0 0 24 24"><path fill="#fff" d="M6.6 10.8a15 15 0 006.6 6.6l2.2-2.2a1 1 0 011-.2 11 11 0 003.6.6 1 1 0 011 1V20a1 1 0 01-1 1A17 17 0 013 4a1 1 0 011-1h3.5a1 1 0 011 1c0 1.2.2 2.5.6 3.6a1 1 0 01-.3 1z"/></svg></div>
    <div><div class="chip-label">CALL US NOW</div><div class="chip-value">555.010.2030</div></div>
  </div>
  <nav class="main-nav abs">
    <span class="current">HOME</span><span>ABOUT US</span><span>PRODUCTS</span><span>FEATURES</span><span>BLOG</span><span>CONTACT US</span>
  </nav>
</header>

<section class="hero abs" role="img" aria-label="Action photo of two football players challenging for a header during a professional match">
  <div class="hero-lower"></div>
</section>
<div class="hero-panel abs">
  <div class="hero-title">Q3 2020 will<br>be the launch<br>of the V1<br>headband</div>
  <span class="btn btn-solid">Read more</span>
</div>
<div class="dots abs"><i></i><i></i><i class="on"></i><i></i><i></i></div>

<section class="mission abs">
  <div class="mission-photo" role="img" aria-label="Blue-toned photo of a player's boot striking a football on turf"></div>
  <span class="tag tag-light">Our mission</span>
  <h2>Helmora – bringing safety to the sports concussion debate</h2>
  <div class="rule"></div>
  <p>Helmora is designing and developing head protection products to reduce the likelihood of concussion when playing sports. Exploring and understanding medical insights, material science and composites research, current and former players experiences and governing bodies guidelines has allowed Helmora to develop the safety, style, form and function requirements of a suitable product to bring to market in Q4 2020.</p>
  <span class="btn btn-white">Read more</span>
</section>

<section class="product abs">
  <span class="tag tag-blue">The product</span>
  <h3>A technology breakthrough in the sport that will protect as well as allow for new data collection and analytics.</h3>
  <p>Our initial product will be simplistic in function and design to ensure we get to market in 2020. Further versions of the product will incorporate data tracking technologies to enhance analytical streams available to players and clubs. Starting with soccer, followed by other markets such as netball and field hockey, where the same issues exist today. We will create a new sector of sports apparel that will serve all communities of sport and allow for new categories of sponsorship and branding.</p>
  <span class="btn btn-solid">Read more</span>
  <div class="product-art" role="img" aria-label="Illustration of the dark grey protective headband"></div>
</section>

<section class="benefits abs">
  <div class="benefit">
    <svg width="48" height="60" viewBox="0 0 48 60" fill="none" stroke="#fff" stroke-width="4" stroke-linecap="round"><circle cx="28" cy="7" r="5" fill="#fff" stroke="none"/><path d="M26 16l-6 20 10 8-2 14M20 36l-8 14M10 24l12-6 8 10 10 2"/></svg>
    <div>Functional &amp;<br>Protective headgear<br>that is appealing</div>
  </div>
  <div class="benefit">
    <svg width="54" height="58" viewBox="0 0 54 58" fill="none" stroke="#fff" stroke-width="2.5"><path d="M4 2h26l10 10v20M40 50v6H4V2"/><path d="M12 18h18M12 26h22M12 34h14M12 42h10"/><circle cx="42" cy="44" r="10"/><path d="M37 44l4 4 6-7"/></svg>
    <div>Allowing for new<br>categories of data<br>capture and analytics</div>
  </div>
  <div class="benefit">
    <svg width="60" height="52" viewBox="0 0 60 52" fill="none" stroke="#fff" stroke-width="2.5"><circle cx="30" cy="16" r="10"/><path d="M14 50c0-10 7-18 16-18s16 8 16 18z"/><circle cx="12" cy="14" r="7"/><circle cx="48" cy="14" r="7"/><path d="M2 40c0-8 4-14 10-14M58 40c0-8-4-14-10-14"/></svg>
    <div>Working group<br>tocarry out<br>intial trials</div>
  </div>
</section>

<section class="features abs">
  <span class="tag tag-blue section-tag">Features</span>
  <div class="feature-grid">
    <div class="feature"><svg width="46" height="46" viewBox="0 0 46 46"><circle cx="23" cy="23" r="14" fill="none" stroke="#1e8ad6" stroke-width="7" stroke-dasharray="6 5"/><circle cx="23" cy="23" r="11" fill="#1e8ad6"/><circle cx="23" cy="23" r="5" fill="#fff"/></svg>A British designed and manufactured unisex headband style head protection product, with a built-in hightech polymer to manage the energy of impacts</div>
    <div class="feature"><svg width="40" height="46" viewBox="0 0 40 46" fill="none" stroke="#1e8ad6" stroke-width="2"><path d="M4 2h20l8 8v16M32 40v4H4V2"/><path d="M10 14h14M10 20h16M10 26h10"/><circle cx="31" cy="35" r="7"/><path d="M28 35l2 2 4-4"/></svg>Available in a range of sizes; and Personalised options and colours.</div>
    <div class="feature"><svg width="46" height="46" viewBox="0 0 46 46" fill="none" stroke="#1e8ad6" stroke-width="2"><path d="M14 4v16M20 2v18M26 4v14M8 10v14c0 6 4 10 10 10h6"/><path d="M32 42V26M26 44V28M20 42V30M38 36V22c0-6-4-10-10-10h-6"/></svg>Acharitable donation will be made from the sale of each product to a head injury or oncussion research related charity.</div>
    <div class="feature"><svg width="52" height="46" viewBox="0 0 52 46" fill="none" stroke="#1e8ad6" stroke-width="2"><circle cx="18" cy="16" r="10" stroke-dasharray="4 2"/><circle cx="18" cy="16" r="4"/><circle cx="36" cy="32" r="10" stroke-dasharray="4 2"/><circle cx="36" cy="32" r="4"/><circle cx="36" cy="8" r="5" stroke-dasharray="3 2"/></svg>The first product will be available Q1 2021. Giving confidence to parents and users that they can play soccer again safely in a post pandemic world.</div>
    <div class="feature"><svg width="46" height="46" viewBox="0 0 46 46" fill="none" stroke="#1e8ad6" stroke-width="2"><path d="M16 30c-5-3-8-8-8-13a15 15 0 0130 0c0 5-3 10-8 13v6H16z"/><path d="M18 40h10M20 44h6"/><circle cx="26" cy="15" r="4"/><path d="M26 8v3M26 19v3M19 15h3M30 15h3"/></svg>A second product incorporating advanced performance tracking technology will be available from late Q1 2021.</div>
    <div class="feature"><svg width="40" height="46" viewBox="0 0 40 46"><path d="M20 4C14 14 8 20 8 28a12 12 0 0024 0c0-8-6-14-12-24z" fill="#1e8ad6"/><path d="M14 28a6 6 0 006 6" stroke="#fff" stroke-width="2.5" fill="none" stroke-linecap="round"/></svg>Washable,<br>antibacterial fabric</div>
    <div class="feature"><svg width="40" height="46" viewBox="0 0 40 46" fill="none" stroke="#1e8ad6" stroke-width="2.5"><path d="M20 4l14 6v12c0 10-6 16-14 20-8-4-14-10-14-20V10z"/><circle cx="20" cy="23" r="8"/><path d="M16 23l3 3 5-6"/></svg>Safety tested</div>
    <div class="feature"><svg width="46" height="46" viewBox="0 0 46 46" fill="none" stroke="#1e8ad6" stroke-width="3"><circle cx="23" cy="23" r="19"/><path d="M4 23h38M23 4c-7 6-7 32 0 38M23 4c7 6 7 32 0 38M8 13h30M8 33h30"/></svg>Environmentally<br>friendly;</div>
    <div class="feature"><svg width="52" height="46" viewBox="0 0 52 46"><path d="M4 20c10 6 24 6 34-6 4-4 8-8 10-10-2 8-6 16-14 20-8 4-20 4-30-4z" fill="#1e8ad6"/><path d="M26 26v10" stroke="#1e8ad6" stroke-width="2"/><path d="M22 34l4 6 4-6z" fill="#1e8ad6"/></svg>Light-weight</div>
    <div class="feature"><svg width="46" height="46" viewBox="0 0 46 46" fill="none" stroke="#1e8ad6" stroke-width="2.2"><path d="M6 22h8v20H6zM14 24l8-12c2-3 6-2 6 2l-2 8h12c3 0 4 3 3 5l-4 12c-1 2-2 3-4 3H14"/><path d="M24 2v5M16 6l3 4M32 6l-3 4"/></svg>Comfortable</div>
  </div>
</section>

<section class="team abs">
  <span class="tag tag-blue section-tag">Our team</span>
  <div class="member" style="left:132px">
    <div class="portrait" role="img" aria-label="Portrait photo of the founder" style="background:radial-gradient(circle at 50% 40%,#c9a58f 0%,#b2302e 70%)"></div>
    <h4>Martin Haworth</h4><div class="role">Founder / CEO</div>
    <p>Martin has a wealth of experience of growing start-ups and exiting businesses, from professional services to technology companies, in recent years Martin has been an executive advisor to many global sporting talents, football clubs, right holders and other sports companies.</p>
    <span class="btn btn-solid">View bio</span>
  </div>
  <div class="member" style="left:451px">
    <div class="portrait" role="img" aria-label="Portrait photo of the co-founder" style="background:radial-gradient(circle at 50% 45%,#e1b9a3 0%,#9ea6ad 70%)"></div>
    <h4>Helen Darby</h4><div class="role">Co –Founder / COO</div>
    <p>Helen has been planning and delivering commercial, large scale transformation projects within people based, high-profile and global environments for the last 15 years. COO to a former UK Prime Minister, transforming his business globally across 30 legal jurisdiction</p>
    <span class="btn btn-solid">View bio</span>
  </div>
  <div class="member" style="left:771px">
    <div class="portrait" role="img" aria-label="Portrait photo of a team member" style="background:radial-gradient(circle at 50% 45%,#d8a88f 0%,#c8c2b4 70%)"></div>
    <h4>Graham Toller</h4><div class="role">CCO</div>
    <p>Graham started his career in retail banking,later experience in corporate and privatebanking. Since leaving the corporateworld in 2007, Graham has been bringingpeople and companies together in enable funding and development of projects across Europe.</p>
    <span class="btn btn-solid">View bio</span>
  </div>
</section>

<section class="distribution abs">
  <span class="tag tag-blue section-tag">Distribution</span>
  <p>From parents to clubs to federations our model is simple; parents of youth players, parents of amateur players, professional players and clubs, academies and all with the support of federations and unions</p>
  <div class="partner" style="left:158px;width:146px;background:#d9d9d9;border-radius:4px;height:40px;top:211px" role="img" aria-label="Partner badge"></div>
  <div class="partner" style="left:368px;width:146px;background:#cfcfcf;border-radius:4px" role="img" aria-label="Partner badge"></div>
  <div class="partner" style="left:577px;width:40px;background:#2b5aa8;border-radius:50%;height:40px;top:211px" role="img" aria-label="Partner badge"></div>
  <div class="partner" style="left:677px;width:126px;background:#4b1d5e;border-radius:4px;height:48px;top:207px" role="img" aria-label="Partner badge"></div>
  <div class="partner" style="left:855px;width:42px;background:#c8cfdc;border-radius:4px" role="img" aria-label="Partner badge"></div>
  <div class="partner" style="left:945px;width:110px;background:#d4dbe6;border-radius:4px;height:44px;top:209px" role="img" aria-label="Partner badge"></div>
</section>

<footer class="site-footer abs">
  <div class="brand">HELMORA</div>
  <div class="col-title" style="left:488px">MENU</div>
  <div class="menu-list">HOME<br>ABOUT US<br>PRODUCTS<br>FEATURES<br>BLOG<br>CONTACT US</div>

  <div class="col-title" style="left:660px">CONTACT US</div>
  <div class="foot-item" style="left:660px;top:99px"><span class="foot-icon"><svg width="10" height="14" viewBox="0 0 10 14"><path d="M5 0a5 5 0 015 5c0 4-5 9-5 9S0 9 0 5a5 5 0 015-5z" fill="#1e8ad6"/><circle cx="5" cy="5" r="2" fill="#fff"/></svg></span><span>2150 Harlow Street<br>Ridgefield, CA 90210</span></div>
  <div class="foot-item" style="left:660px;top:161px"><span class="foot-icon"><svg width="12" height="12" viewBox="0 0 24 24"><path fill="#1e8ad6" d="M6.6 10.8a15 15 0 006.6 6.6l2.2-2.2a1 1 0 011-.2 11 11 0 003.6.6 1 1 0 011 1V20a1 1 0 01-1 1A17 17 0 013 4a1 1 0 011-1h3.5a1 1 0 011 1c0 1.2.2 2.5.6 3.6a1 1 0 01-.3 1z"/></svg></span><span>Call Us<br>555.010.2030</span></div>
  <div class="foot-item" style="left:660px;top:223px"><span class="foot-icon"><svg width="13" height="10" viewBox="0 0 13 10"><rect x=".5" y=".5" width="12" height="9" fill="#1e8ad6"/><path d="M.5 .5l6 5 6-5" stroke="#fff" fill="none"/></svg></span><span>E mail Us<br>info@helmora.com</span></div>

  <div class="col-title" style="left:947px">FOLLOW US</div>
  <div class="foot-item" style="left:947px;top:99px"><span class="foot-icon"></span><span>Like us on<br>FRIENDBOOK</span></div>
  <div class="foot-item" style="left:947px;top:161px"><span class="foot-icon"></span><span>Follow us on<br>CHIRPER</span></div>
  <div class="foot-item" style="left:947px;top:223px"><span class="foot-icon"></span><span>Follow us on<br>WORKLINK</span></div>

  <div class="copyright">Copyright © 2020 All Rights Reserved</div>
</footer>

</body>
</html>
```